KVR Biz Cards

We are a property management company that manages luxury level residential estates. As such, we need a business card design that gives a high end feel. The idea at the moment is to list the services offered on the back of the card, and our company information on the front of the card.

Services for the back of the card are as follows:
Professional Property Management service, Home Hosting & Concierge Service, Holliday Home / Income Property Management

```html
<!DOCTYPE html>
<html lang="en">
<head>
<meta charset="utf-8">
<title>KVR Business Cards</title>
<link href="https://fonts.googleapis.com/css2?family=Arimo:wght@400;700&family=Montserrat:wght@600;700&display=swap" rel="stylesheet">
<style>
  :root {
    --stage: #3a3a3c;
    --card-dark: #0b0b0b;
    --card-light: #ffffff;
    --bronze: #8a5a2b;
    --ink: #111111;
    --muted: #6f6f6f;
    --soft-white: #f2f2f2;
    --emboss: #2a2a2a;
  }
  * { box-sizing: border-box; margin: 0; padding: 0; }
  html, body { width: 1200px; height: 976px; overflow: hidden; }
  body {
    background: var(--stage);
    font-family: "Arimo", Arial, sans-serif;
    position: relative;
  }
  .card {
    position: absolute;
    width: 700px;
    height: 400px;
    box-shadow: 0 10px 30px rgba(0,0,0,0.45);
  }
  /* Back side */
  .card--back { left: 150px; top: 58px; background: var(--card-dark); }
  .back-mark {
    position: absolute;
    right: 70px;
    top: 60px;
    font-family: "Montserrat", sans-serif;
    font-weight: 700;
    font-size: 96px;
    letter-spacing: 8px;
    color: var(--emboss);
  }
  .services { position: absolute; left: 70px; bottom: 58px; }
  .services-title {
    color: var(--bronze);
    font-weight: 700;
    font-size: 26px;
    letter-spacing: 1px;
    margin-bottom: 10px;
  }
  .services-list { list-style: none; }
  .services-list li {
    display: flex;
    align-items: center;
    gap: 10px;
    color: var(--soft-white);
    font-size: 19px;
    line-height: 1.45;
  }
  .tick { width: 18px; height: 18px; flex: none; }

  /* Front side */
  .card--front { left: 350px; top: 518px; background: var(--card-light); }
  .brand { position: absolute; left: 60px; top: 48px; }
  .brand-mark {
    display: flex;
    align-items: center;
    gap: 12px;
    color: var(--bronze);
    font-family: "Montserrat", sans-serif;
    font-weight: 700;
    font-size: 52px;
    letter-spacing: 4px;
    margin-left: 70px;
  }
  .brand-square { width: 22px; height: 22px; background: var(--bronze); }
  .brand-name {
    margin-top: 14px;
    font-family: "Montserrat", sans-serif;
    font-weight: 700;
    font-size: 27px;
    color: var(--ink);
    letter-spacing: 0.5px;
  }
  .brand-tagline {
    font-family: "Montserrat", sans-serif;
    font-weight: 600;
    font-size: 16px;
    color: var(--bronze);
    letter-spacing: 0.6px;
    margin-top: 2px;
  }
  .person { position: absolute; right: 50px; top: 70px; text-align: right; }
  .person-name { color: var(--bronze); font-weight: 700; font-size: 24px; }
  .person-role { color: var(--muted); font-size: 16px; margin-top: 2px; }
  .edge-bar {
    position: absolute; right: 0; top: 64px;
    width: 12px; height: 44px; background: var(--bronze);
  }
  .contact { position: absolute; left: 60px; bottom: 40px; color: var(--muted); }
  .address { font-size: 18px; line-height: 1.35; margin-bottom: 14px; }
  .contact-line {
    display: flex; align-items: center; gap: 8px;
    font-size: 18px; line-height: 1.45;
  }
  .icon { width: 15px; height: 15px; flex: none; }
</style>
</head>
<body>

<section class="card card--back">
  <div class="back-mark">KVR</div>
  <div class="services">
    <h2 class="services-title">SERVICES:</h2>
    <ul class="services-list">
      <li><svg class="tick" viewBox="0 0 18 18"><circle cx="9" cy="9" r="9" fill="#8a5a2b"/><path d="M5 9.5l2.6 2.6L13 6.6" fill="none" stroke="#0b0b0b" stroke-width="2"/></svg>Professional Property Management service,</li>
      <li><svg class="tick" viewBox="0 0 18 18"><circle cx="9" cy="9" r="9" fill="#8a5a2b"/><path d="M5 9.5l2.6 2.6L13 6.6" fill="none" stroke="#0b0b0b" stroke-width="2"/></svg>Home Hosting &amp; Concierge Service,</li>
      <li><svg class="tick" viewBox="0 0 18 18"><circle cx="9" cy="9" r="9" fill="#8a5a2b"/><path d="M5 9.5l2.6 2.6L13 6.6" fill="none" stroke="#0b0b0b" stroke-width="2"/></svg>Holliday Home / Income Property Management</li>
    </ul>
  </div>
</section>

<section class="card card--front">
  <div class="brand">
    <div class="brand-mark"><span class="brand-square"></span>KVR</div>
    <div class="brand-name">KAVERA MANAGEMENT</div>
    <div class="brand-tagline">Crafted to Keep Every Home at Ease</div>
  </div>

  <div class="person">
    <div class="person-name">DANIEL HARROW</div>
    <div class="person-role">President</div>
  </div>
  <div class="edge-bar"></div>

  <div class="contact">
    <p class="address">Harbour Court 4, Level 3<br>P.O. Box 00000, Marina City</p>
    <p class="contact-line">
      <svg class="icon" viewBox="0 0 16 16"><path d="M3.5 1.5l2.5 0 1 3.5-1.8 1.2a9 9 0 0 0 4.6 4.6L11 9l3.5 1v2.5c0 1-1 2-2 2C6.5 14.5 1.5 9.5 1.5 3.5c0-1 1-2 2-2z" fill="#8a5a2b"/></svg>000 555 0199
    </p>
    <p class="contact-line">
      <svg class="icon" viewBox="0 0 16 16"><rect x="1" y="3" width="14" height="10" fill="#8a5a2b"/><path d="M1 3l7 6 7-6" fill="none" stroke="#fff" stroke-width="1.4"/></svg>info@kaveramanagement.com
    </p>
    <p class="contact-line">
      <svg class="icon" viewBox="0 0 16 16"><circle cx="8" cy="8" r="7" fill="none" stroke="#8a5a2b" stroke-width="1.6"/><ellipse cx="8" cy="8" rx="3" ry="7" fill="none" stroke="#8a5a2b" stroke-width="1.2"/><path d="M1 8h14" stroke="#8a5a2b" stroke-width="1.2"/></svg>www.kaveramanagement.com
    </p>
  </div>
</section>

</body>
</html>
```